Apothecary Staffing Partners, LLC
Local. National. Nationwide.
• 1 mars 2011 21:09 korunthavel
hi sir
who is the winner
• 26 février 2011 04:46 ApothecaryStaffingPartners
Reopened to get final design versions. Thank you to all!
• 24 février 2011 00:00 korunthavel
sir check your private message
i sent one link
• 23 février 2011 21:39 korunthavel
i complete all changes
but contest is closed
what i do
any other option sir
• 20 février 2011 20:39 ApothecaryStaffingPartners
Hi Designers,
I apologize for the delay with the project. I will provide timely feedback moving forward.
Here are my likes and dislikes:
WHAT I LIKE:
1) Please definately use the COLOR scheme used in the following website:
http://demo7.layoutsample-hub.net/qz_58214/index.html
The blues are perfect, also the shadings are great. Also love the color of the orange. Also love the other colors (greens, light blues) and the way they have color gradients in them and shadowing below them. The white and lighter blue lettering also work well. Just please make sure that the blue lettering is different enough from the background that it is easy to read.
I also like on this website that it appears as if the webpage takes up the entire computer monitor screen, even if it does not on some monitors.
2) Pictures of our office
3) Please use the Museo fonts throughout the website, as Calvin did.
4) Use of the attached Flash Logo
5) In # 63:
I like the way the tabs for the links are rounded off, and I like that they are shadowed below the tabs. I like the way they are spaced evenly across top bar.
I like the way the contact info is presented on the top right, with the icons. (Only need to change info to: Office 555-555-5473 Fax 555-555-5473 Web 555-555-5473.example “Just Think All 5’s and 473..Every Dispensary Request..Bullseye”)
I like the targets on the picture of the world.
I like the large ASP outlined in white and shadowed.
I like the use of the orange lettering to add emphasis on certain words.
I like the ability to scroll for more information, so that the page remains uncluttered.
I like the way the affiliations logos are shadowed. Would like to see them rounded off like the tabs on the top of the page, though.
Use of office picture in the contact info area.
6) In #60:
I like that Calvin used my fonts (Museo) in differing weights throughout the webpage.
I like the use of the orange faded lines to match the logo.
I like the way the site map with the ASP was done at the bottom.
I like the way the top bar with the logo goes with the rest of the page. It does not look separate from the rest of the page, looks like it was meant to be there.
I like that the page is wide. I like the uncluttered feel.
I like the way the Keep Updated and the receive our newsletter with the Go button was done.
It is my goal to make the site uniform with the logo. Calvin did a good job at this. He used the Museo fonts, the faded orange lines, the ASP.
I like the freshness and new idea of the blocks with the phrases. Another idea would have been to make the blocks look like prescription pads of paper.
7) In #37:
I like the middle section. Like the way the information scrolls, like the use of the office photo. I also like the “Latest Jobs” section on the right.
I like the contact info up top.
On the map bar, I like the way the local national worldwide is in a darker stripe across the whole bar. I like the way there is a golden shadow in this area. I also like the tabs with the phrases in this area.
I like the links to Facebook, Twitter, and Linked In.
WHAT I DO NOT LIKE:
1) Pictures of people shaking hands. Most pictures of people in general. Too common on recruiting websites.
2) In #63:
The logo on top in the bar with the contact info seems somehow not to go well with the rest of the page. Looks a bit disjointed. If you want to try a dark background for this top bar, feel free to try changing the logo colors to make it work.
Too much info in the middle. Looks a bit cluttered.
The web page should blend with the background of the monitor screen.
3) In #60:
Did not like that the color of the lettering was so close to the background color that it was hard to read.
General Comments:
The contact information should read:
Office 555-555-5473, Fax 555-555-5473, Web 555-555-5473.example, “Just Think All 5’s and 473..Every Dispensary Request..Bullseye” . This information could almost be a logo in itself if done right. Use Museo Fonts.
Other Ideas for an unusual, unique website:
Although I do like some the things submitted, I am still open to new ideas. One site I like is at http://demo7.layoutsample-hub.net/qz_59367/index.html
Another idea to be creative is to use prescription pads (the notepads that doctors use to write for patient’s medications) or mortar and pestles in a creative way on the site.
Another idea: Make the page look like a patient’s hospital chart, with tabs on the chart for the different web pages. Similar to when a person may use a diary for a personal website, or a photographer may use a photo album. They are called medical charts, and also there are medical chart carts. An example of a medical chart cart picture is uploaded so you know what I’m referring to.
• 11 février 2011 07:57 korunthavel
• 10 février 2011 09:51 Rizwan
Hi,
Any updates regarding contest?
Regards
Qorvane Studio
Designers: Do not engage yourselves into arguments, if anyone has any rip off claims email us at report@pixelquarry.example
• 30 janvier 2011 02:55 artz4upixel
Count to me #34, #35
• 29 janvier 2011 14:30 mora318
Yes we can use your flash logo on your homepage but how can we show animation? Pixelquarry doesn't allow swf file or any animated object
leyla
• 29 janvier 2011 08:09 ApothecaryStaffingPartners
Please, no pictures of people or shaking hands on the homepage.
Can anyone use my attached flash logo?
• 29 janvier 2011 03:33 Rizwan
:@ ambrosk.
you are copy My concept. i will report about this design.
• 28 janvier 2011 18:03 ApothecaryStaffingPartners
You can make the logo white or use different colors if you need to in order to make it look good on a dark background.
• 28 janvier 2011 18:01 ApothecaryStaffingPartners
Please read the brief. Just to reiterate:
Want to integrate flash logo. Files are attached.
Definately want a Dark Background - Dark Blue or Black is a good choice. Definately want rich, bold colors offsetting the dark background.
Want an uncluttered, clean feel.
Want a refreshing layout. Not the same as other recruiting websites, that seem to be all squared off in its presentation.
My contact info is "All 5's and a 4-7-3", meaning office # is 555-555-5473, fax is 555-555-5473, website can be accessed thru www.555-555-5473.example . Want to emphasize this on the hompage somehow because it is easy to remember. Catchphrase could be “All 5’s and a 4-7-3 Every Dispensary Request. Bullseye."
Comments on what I Do Not want:
No pictures of smiling people on home page. Too ordinary. Most recruiting websites have this.
Pictures of people shaking hands
Images of shaking hands
Goofy pictures of employees
Most pictures of people.
Please read the brief for examples of work that I like.
Thank you!
• 28 janvier 2011 12:13 ApothecaryStaffingPartners
I apologize, but I thought that you could get the logo files from TWB since they created it. I have uploaded the logo files, as well as the flash logo file. If you think my logo would look better with a different font, I am open to looking at it. But, this project is for a web page.
• 28 janvier 2011 04:49 brightfolk
Hello
No logo or font attachments sent.
please upload to work upon.
Thanks
• 27 janvier 2011 16:20 kornelwest
where is the logo that you have for your company?
• 26 janvier 2011 23:25 tint4forms
@Markwell.. Ouch! :)
• 26 janvier 2011 13:28 ApothecaryStaffingPartners

```html
<!DOCTYPE html>
<html lang="en">
<head>
<meta charset="utf-8">
<title>Apothecary Staffing Partners, LLC</title>
<link rel="stylesheet" href="https://fonts.googleapis.com/css2?family=Exo+2:wght@400;600;700;800&family=Open+Sans:wght@400;600&display=swap">
<style>
:root{
  --page:#0a121d;
  --bar:#0e1826;
  --navy:#0b2550;
  --blue:#1d5fb8;
  --sky:#5fa3ea;
  --orange:#f08a1c;
  --white:#ffffff;
  --text:#c9d3df;
  --muted:#5f6e80;
  --line:#2a3646;
}
*{box-sizing:border-box;margin:0;padding:0}
html,body{width:1200px;height:1023px;overflow:hidden}
body{background:var(--page);font-family:"Open Sans",Arial,sans-serif;color:var(--text);position:relative}
.topbar{position:absolute;left:0;top:0;width:1200px;height:112px;background:linear-gradient(#111c2b,#0c1420);border-bottom:2px solid var(--orange)}
.brand{position:absolute;left:145px;top:30px;display:flex;align-items:center;gap:12px}
.brand-mark{font-family:"Exo 2",sans-serif;font-weight:800;font-size:46px;color:var(--orange);line-height:1}
.brand-name{font-family:"Exo 2",sans-serif;font-weight:600;font-size:15px;color:var(--sky);line-height:1.15;width:170px}
.tagline{position:absolute;right:120px;top:28px;font-family:"Exo 2",sans-serif;font-size:15px;color:var(--sky)}
.nav{position:absolute;right:120px;top:62px;display:flex;gap:26px;font-family:"Exo 2",sans-serif;font-weight:700;font-size:18px}
.nav a{color:var(--sky);text-decoration:none}
.hero{position:absolute;left:0;top:114px;width:1200px;height:274px;background:radial-gradient(ellipse at 55% 55%,#2c6fd0 0%,#123a7c 45%,#081a38 100%)}
.hero-map{position:absolute;inset:0}
.hero-band{position:absolute;left:0;top:84px;width:1200px;height:96px;background:rgba(5,15,35,.55)}
.hero-title{position:absolute;left:172px;top:84px;font-family:"Exo 2",sans-serif;font-weight:700;font-size:20px;color:var(--white);white-space:nowrap}
.hero-motto{position:absolute;left:172px;top:114px;font-family:"Exo 2",sans-serif;font-weight:800;font-size:29px;color:var(--white);white-space:nowrap}
.pillars{position:absolute;left:618px;top:20px;display:flex;align-items:flex-end;gap:16px;height:240px}
.pillar{width:84px;background:linear-gradient(90deg,#eef3f9,#b9c6d6);border-radius:4px;box-shadow:0 12px 18px rgba(0,0,0,.45);padding:14px 6px;font-family:"Exo 2",sans-serif;font-weight:700;font-size:14px;line-height:1.2;color:#1c2c44;transform:skewY(-4deg);overflow:hidden}
.pillar .tight{font-size:10px}
.pillar.p1{height:150px;width:88px;font-size:13px}.pillar.p2{height:190px;font-size:17px}.pillar.p3{height:110px;width:62px;font-size:11px}.pillar.p4{height:175px}
.newsbar{position:absolute;left:145px;top:392px;width:935px;height:52px;background:linear-gradient(#101b2a,#0c1522);border:1px solid var(--line)}
.hiring{position:absolute;left:14px;top:6px;font-family:"Exo 2",sans-serif;font-size:21px;color:#2c4260}
.hiring small{display:block;font-size:11px;color:#2c4260;margin-top:-2px}
.keep{position:absolute;left:520px;top:8px;font-family:"Exo 2",sans-serif;font-weight:700;font-size:17px;color:var(--blue)}
.keep small{display:block;font-weight:400;font-size:11px;color:var(--muted)}
.field{position:absolute;left:660px;top:10px;width:170px;height:12px;background:#1a2535;border:1px solid #263347}
.field.f2{top:28px}
.go{position:absolute;left:858px;top:9px;width:50px;height:32px;background:linear-gradient(#1f3e6c,#132845);border-radius:4px;color:var(--sky);font-family:"Exo 2",sans-serif;font-weight:700;font-size:17px;text-align:center;line-height:32px}
.columns{position:absolute;left:145px;top:490px;width:935px;height:300px}
.col{position:absolute;top:0}
.col h2{font-family:"Exo 2",sans-serif;font-weight:600;font-size:21px;color:var(--white);margin-bottom:14px}
.col.news{left:12px;width:260px}
.col.service{left:335px;width:260px}
.col.about{left:636px;width:290px}
.divider{position:absolute;top:10px;width:2px;height:270px;background:linear-gradient(var(--orange),rgba(240,138,28,0))}
.divider.d1{left:300px}.divider.d2{left:610px}
.news-item{background:linear-gradient(90deg,#10233f,#0c1830);padding:7px 10px;margin-bottom:10px;width:250px}
.news-item p{font-size:11.5px;line-height:1.25;color:#a9bdd4}
.news-item time{display:block;font-size:10px;color:var(--white);margin-top:4px}
.service ul{list-style:none}
.service li{font-size:12px;line-height:1.25;color:#a9bdd4;margin-bottom:9px}
.about p{font-size:12px;line-height:1.3;color:#a9bdd4;margin-bottom:10px}
.about p.faded{color:#1f3f70}
.rule{position:absolute;left:125px;width:950px;height:1px;background:#3a4656}
.rule.r1{top:795px}.rule.r2{top:893px}
.partners{position:absolute;left:485px;top:812px;display:flex;gap:18px}
.badge{height:62px;background:#f1f3f6;border-radius:6px;box-shadow:0 5px 8px rgba(0,0,0,.5)}
.footer-mark{position:absolute;left:128px;top:912px;font-family:"Exo 2",sans-serif;font-weight:800;font-size:44px;color:#7c8694}
.footer-links{position:absolute;left:245px;top:916px;font-size:12px;color:#a9bdd4}
.footer-links span{margin:0 6px;color:#5f6e80}
.copyright{position:absolute;left:245px;top:942px;font-size:10px;color:#8090a3}
</style>
</head>
<body>
<header class="topbar">
  <div class="brand"><span class="brand-mark">ASP</span><span class="brand-name">Apothecary Staffing Partners</span></div>
  <div class="tagline">All 5's and a 4-7-3 Every Dispensary Request. Bullseye.</div>
  <nav class="nav"><a href="#">Home</a><a href="#">Employer</a><a href="#">Candidate</a><a href="#">Recruiter</a><a href="#">ASP Staff</a><a href="#">Contact Us</a></nav>
</header>

<section class="hero">
  <div class="hero-map" role="img" aria-label="Blue world map with glowing light behind the headline"></div>
  <div class="hero-band"></div>
  <h1 class="hero-title">Apothecary Staffing Partners</h1>
  <p class="hero-motto">Local. National. Worldwide.</p>
  <div class="pillars">
    <div class="pillar p1">In Your <span class="tight">Neighborhood</span> Around the World</div>
    <div class="pillar p2">Behold the Power of ASP</div>
    <div class="pillar p3">Set the Bar! It's your career</div>
    <div class="pillar p4">Temporary Staffing Permanent Solutions</div>
  </div>
</section>

<section class="newsbar">
  <div class="hiring">Pharmacy Management Positions Hiring<small>Now hiring in selected regions</small></div>
  <div class="keep">Keep Update<small>Receive our newsletter</small></div>
  <div class="field"></div><div class="field f2"></div>
  <div class="go">Go</div>
</section>

<main class="columns">
  <div class="col news">
    <h2>ASP News</h2>
    <article class="news-item"><p>New Book Reveals Reasons Behind Record-Breaking Employee Dissatisfaction</p><time>Tuesday, January 18, 2011</time></article>
    <article class="news-item"><p>New Book Reveals Reasons Behind Record-Breaking Employee Dissatisfaction</p><time>Tuesday, January 18, 2011</time></article>
    <article class="news-item"><p>New Book Reveals Reasons Behind Record-Breaking Employee Dissatisfaction</p><time>Tuesday, January 18, 2011</time></article>
  </div>
  <div class="divider d1"></div>
  <div class="col service">
    <h2>Our Service</h2>
    <ul>
      <li>Accounting / Financial Services</li>
      <li>Chemical Process</li>
      <li>Hardware / Software / Electronics</li>
      <li>Healthcare</li>
      <li>Information Technology</li>
      <li>Manufacturing / Production</li>
      <li>Sales / Marketing / Business Development</li>
      <li>Strategic Management including Executive Management and Human Resources</li>
      <li>Supply Chain</li>
    </ul>
  </div>
  <div class="divider d2"></div>
  <div class="col about">
    <h2>About ASP</h2>
    <p>ASP is a professional recruitment and staffing firm, specializing in permanent placement and contract staffing of pharmacists and upper level pharmacy management.</p>
    <p>We consistently hit the mark, delivering a healthcare professional who is fulfilled in their career, functioning in sync with the client organization to ensure effective business operation and quality patient care.</p>
    <p class="faded">Read more about our approach and the markets we serve across the country.</p>
  </div>
</main>

<div class="rule r1"></div>
<div class="partners">
  <div class="badge" style="width:92px"></div>
  <div class="badge" style="width:70px"></div>
  <div class="badge" style="width:75px"></div>
  <div class="badge" style="width:138px"></div>
  <div class="badge" style="width:102px"></div>
</div>
<div class="rule r2"></div>

<footer>
  <div class="footer-mark">ASP</div>
  <div class="footer-links">Home<span>|</span>Employer<span>|</span>Candidate<span>|</span>Recruiter<span>|</span>ASP Staff<span>|</span>Contact Us</div>
  <div class="copyright">Copyright © 2010 Markcraft Studio, Inc. markcraft.example. All Rights Reserved.</div>
</footer>
</body>
</html>
```